International Sex Coach needs a Book Cover in less than 3 days

I need a cover design for my book coming out next week titled "A Quiet Atlas Toward Closeness". The book explores the origins of our cultural ideas about sexuality and taboo and is interwoven with personal memoir.
The reader must feel that they are being pulled into an intimate sexual story, but also a deeper understanding of sex itself. Like they are jumping into bed with me, you might say. I would like the title to take up the majority of the space over an image of 3D, very real bed sheets, but I am open to your ideas. I haven't purchased any images yet, but there are a few below I was drawn to.
In its essence, this book is designed to reeducate the reader about sexuality and open them up to a new paradigm of sexual wellness.
The author name is Mirela Oswin. Page must also include the phrase: a revolutionary new approach to sexuality, relationship and love.
Size 6" x 9" (15.24 x 22.86 cm)
Thanks!

Reason: I need more time to review the designs and give feedback.

Target Market(s)

Sexually active men and women.

Industry/Entity Type

Wellness

Font styles to use
Serif

```html
<!DOCTYPE html>
<html lang="en">
<head>
<meta charset="utf-8">
<title>A Quiet Atlas Toward Closeness — Cover Wrap</title>
<link rel="stylesheet" href="https://fonts.googleapis.com/css2?family=Cormorant+Garamond:wght@300;400;500&display=swap">
<style>
  :root {
    --velvet-deep: #8e0a0c;
    --velvet-mid: #c8161a;
    --velvet-bright: #e2262a;
    --velvet-shadow: #6a0608;
    --type-white: #ffffff;
    --type-soft: rgba(255, 255, 255, 0.9);
    --fold-line: rgba(255, 255, 255, 0.85);
  }
  * { margin: 0; padding: 0; box-sizing: border-box; }
  html, body {
    width: 1200px;
    height: 940px;
    overflow: hidden;
    background: var(--velvet-mid);
  }
  .cover-wrap {
    position: relative;
    width: 1200px;
    height: 940px;
    overflow: hidden;
    font-family: "Cormorant Garamond", Georgia, "Times New Roman", serif;
    color: var(--type-white);
  }
  .velvet-backdrop {
    position: absolute;
    inset: 0;
    background:
      radial-gradient(ellipse 420px 260px at 1080px 720px, var(--velvet-shadow) 0%, transparent 70%),
      radial-gradient(ellipse 600px 180px at 300px 330px, rgba(255, 80, 80, 0.35) 0%, transparent 70%),
      radial-gradient(ellipse 520px 160px at 420px 620px, rgba(90, 0, 0, 0.45) 0%, transparent 70%),
      radial-gradient(ellipse 700px 200px at 260px 800px, rgba(255, 70, 70, 0.3) 0%, transparent 70%),
      linear-gradient(160deg, var(--velvet-bright) 0%, var(--velvet-mid) 40%, var(--velvet-deep) 75%, var(--velvet-mid) 100%);
  }
  .spine-guide {
    position: absolute;
    top: 0;
    width: 0;
    height: 940px;
    border-left: 1.5px dashed var(--fold-line);
  }
  .spine-guide--left { left: 572px; }
  .spine-guide--right { left: 626px; }
  .spine-text {
    position: absolute;
    left: 587px;
    writing-mode: vertical-rl;
    transform: rotate(180deg);
    font-weight: 400;
    white-space: nowrap;
    line-height: 1;
  }
  .spine-text--title { top: 90px; font-size: 21px; letter-spacing: 0.3px; }
  .spine-text--author { bottom: 60px; font-size: 17px; letter-spacing: 1.5px; text-transform: uppercase; }
  .front-title {
    position: absolute;
    left: 706px;
    top: 132px;
    font-weight: 400;
    line-height: 1;
  }
  .front-title span { display: block; }
  .front-title__lead { font-size: 34px; margin-bottom: 0; }
  .front-title__key { font-size: 84px; line-height: 0.88; letter-spacing: 1px; }
  .front-title__line { font-size: 64px; line-height: 0.98; }
  .front-tagline {
    position: absolute;
    left: 708px;
    top: 420px;
    width: 400px;
    font-size: 21px;
    font-weight: 400;
    font-style: italic;
    line-height: 1.3;
    color: var(--type-soft);
  }
  .front-author {
    position: absolute;
    left: 706px;
    bottom: 70px;
    font-size: 30px;
    font-weight: 500;
    letter-spacing: 4px;
    text-transform: uppercase;
  }
</style>
</head>
<body>
  <main class="cover-wrap">
    <div class="velvet-backdrop" role="img" aria-label="Photograph of draped red velvet sheets in soft folds across the full wrap"></div>

    <div class="spine-guide spine-guide--left"></div>
    <div class="spine-guide spine-guide--right"></div>

    <p class="spine-text spine-text--title">A Quiet Atlas Toward Closeness</p>
    <p class="spine-text spine-text--author">Mirela Oswin</p>

    <h1 class="front-title">
      <span class="front-title__lead">A Quiet</span>
      <span class="front-title__key">ATLAS</span>
      <span class="front-title__line">Toward</span>
      <span class="front-title__line">Closeness</span>
    </h1>

    <p class="front-tagline">A revolutionary new approach to sexuality, relationship and love</p>

    <p class="front-author">Mirela Oswin</p>
  </main>
</body>
</html>
```